Unique and original Business Card for Financial Services Business

I have moved premises and need to change the detail on my business card so thought now is a good time for a re-design. Looking for something professional and modern with colours to fit in with out logo. Like the idea of foil or embossing if that works but not a must have but I do want something that stands out and that I could not design myself.

Once business card is designed I will also be looking to get letterhead and flyers done but want the business card concept in place first.

The majority of designs I am receiving are generic and template based. I am looking for something unique and original. We have some great design elements in our logo, think outside the box and show me something that stands out from the crowd.

Target Market(s)

Business Professionals

Industry/Entity Type

Finance

Contact Information for Business Card

Name: Delia Norwood Phone 0473 958 162 Address PO Box 8617 Mossvale NSW 2389 Email info@steadyharbourfinancialservices.com.au website www.steadyharbourfinancialservices.com.au

Font styles to use
Other font styles liked:
• Ralway

Requirements
Should not have
• No black backgrounds please

```html
<!DOCTYPE html>
<html lang="en">
<head>
<meta charset="utf-8">
<title>Steady Harbour Financial Services – Business Card</title>
<link rel="stylesheet" href="https://fonts.googleapis.com/css2?family=Raleway:wght@300;400&family=Great+Vibes&display=swap">
<style>
  :root {
    --backdrop: #84dcbc;
    --card-white: #ffffff;
    --mark-tint-light: #e6ecf3;
    --mark-tint-fade: #f4f7fa;
    --navy: #07497c;
    --navy-tint: #2d6592;
    --teal: #23998a;
    --ink: #1f1f22;
    --contact-blue: #1d5d8c;
    --rule-grey: #c9c9c9;
    --accent-green: #38c98d;
    --white: #ffffff;
  }
  * { margin: 0; padding: 0; box-sizing: border-box; }
  html, body { width: 1000px; height: 1200px; overflow: hidden; }
  body {
    background: var(--backdrop);
    position: relative;
    font-family: "Raleway", "Helvetica Neue", Arial, sans-serif;
  }
  .card {
    position: absolute;
    left: 160px;
    width: 638px;
    height: 377px;
    overflow: hidden;
    box-shadow: 5px 5px 4px rgba(40, 70, 60, 0.45);
  }
  .card--front {
    top: 198px;
    background: var(--card-white);
    border-top-left-radius: 68px;
  }
  .card--back {
    top: 653px;
    background: var(--navy);
    border-top-right-radius: 68px;
  }
  .brand-watermark { position: absolute; display: block; }
  .card--front .brand-watermark { left: 99px; top: 0; width: 437px; height: 377px; }
  .card--back .brand-watermark { left: 0; top: 27px; width: 374px; height: 322px; }

  .wordmark {
    position: absolute;
    left: 0;
    right: 0;
    top: 118px;
    text-align: center;
    color: var(--teal);
    font-weight: 300;
  }
  .wordmark__dot {
    display: block;
    width: 26px;
    height: 26px;
    margin: 0 auto 38px;
    border-radius: 50%;
    background: var(--teal);
  }
  .wordmark__name {
    display: block;
    font-size: 34px;
    line-height: 34px;
    letter-spacing: -0.5px;
  }
  .wordmark__sub {
    display: block;
    margin-top: 4px;
    font-size: 17px;
    letter-spacing: 11px;
    padding-left: 11px;
  }

  .contact-row {
    position: absolute;
    left: 57px;
    top: 340px;
    display: flex;
    align-items: center;
    font-size: 12.5px;
    color: var(--contact-blue);
    white-space: nowrap;
  }
  .contact-row__item { display: flex; align-items: center; gap: 5px; }
  .contact-row__divider {
    width: 1.5px;
    height: 26px;
    background: var(--rule-grey);
    margin: 0 17px;
  }

  .holder {
    position: absolute;
    left: 289px;
    top: 138px;
    color: var(--white);
  }
  .holder__name {
    font-family: "Great Vibes", cursive;
    font-size: 56px;
    line-height: 70px;
    font-weight: 400;
  }
  .holder__contacts {
    display: flex;
    align-items: center;
    font-size: 10.5px;
    font-weight: 300;
    white-space: nowrap;
    margin-top: 2px;
  }
  .holder__divider {
    width: 1.5px;
    height: 14px;
    background: var(--accent-green);
    margin: 0 7px;
  }
</style>
</head>
<body>

<section class="card card--front" aria-label="Business card front">
  <svg class="brand-watermark" viewBox="0 0 437 377" role="img" aria-label="Faint oversized brand mark decoration">
    <defs>
      <linearGradient id="front-fade" x1="0" y1="0" x2="1" y2="0">
        <stop offset="0" stop-color="var(--mark-tint-light)"/>
        <stop offset="1" stop-color="var(--mark-tint-fade)"/>
      </linearGradient>
    </defs>
    <rect width="437" height="377" fill="url(#front-fade)"/>
  </svg>

  <div class="wordmark">
    <span class="wordmark__dot"></span>
    <span class="wordmark__name">STEADY HARBOUR</span>
    <span class="wordmark__sub">Financial Services</span>
  </div>

  <div class="contact-row">
    <span class="contact-row__item">
      <svg width="11" height="18" viewBox="0 0 11 18" aria-hidden="true">
        <path d="M5.5 0C2.5 0 0.5 2.2 0.5 5c0 3.2 5 9 5 9s5-5.8 5-9C10.5 2.2 8.5 0 5.5 0z" fill="var(--teal)"/>
        <path d="M1.5 15.5c1 1.2 7 1.2 8 0" stroke="var(--teal)" stroke-width="1.3" fill="none"/>
      </svg>
      PO Box 8617 Mossvale NSW 2389
    </span>
    <span class="contact-row__divider"></span>
    <span class="contact-row__item">
      <svg width="16" height="14" viewBox="0 0 16 14" aria-hidden="true">
        <rect x="0" y="0" width="16" height="11" rx="1" fill="var(--teal)"/>
        <rect x="7" y="11" width="2" height="2" fill="var(--teal)"/>
        <rect x="5" y="13" width="6" height="1" fill="var(--teal)"/>
      </svg>
      www.steadyharbourfinancialservices.com.au
    </span>
  </div>
</section>

<section class="card card--back" aria-label="Business card back">
  <svg class="brand-watermark" viewBox="0 0 374 322" role="img" aria-label="Large tinted brand mark decoration">
    <rect width="374" height="322" fill="var(--navy-tint)" opacity="0.75"/>
  </svg>

  <div class="holder">
    <h1 class="holder__name">Delia Norwood</h1>
    <div class="holder__contacts">
      <span>0473 958 162</span>
      <span class="holder__divider"></span>
      <span>info@steadyharbourfinancialservices.com.au</span>
    </div>
  </div>
</section>

</body>
</html>
```